Design a styled business card for an intimacy and attachment psychologist

I am a Psychologist providing online therapy to patients across the United States. My work is interpersonal and emotion-focused, with an emphasis on the client-therapist relationship. My primary areas of work are very personal, including sexuality and gender, abuse and trauma, and grief and loss. My target audience will be adults of all ages 18+.
My business card should convey a warm and inviting feeling of professionalism that is also casual and comfortable.
The front should be fairly simple and professional, consisting of:
- My name, Dr. Rosalind Petrakis
- My title, Licensed Psycholigist
- My logo
On either the front or the back, my contact information should be listed:
- ros@drrospetrakis.example
- 555.014.7788
- drrospetrakis.example
On the rear, I would like a description of the areas that I specialize in. This can be formatted in any way that appears stylistically interesting.
Individual and Couples
Relationships and Infidelity
Sexual Health & Aging
Gender Identity & Sexual Orientation
Abuse and Trauma
Sexual Compulsivity & Addiction
Sexual Dysfunction
Target Market(s)
My target audience will be adults of all ages 18+.
Industry/Entity Type
Psychology
Contact Information for Business Card
The front should be fairly simple and professional, consisting of: - My name, Dr. Rosalind Petrakis - My title, Licensed Psycholigist - My logo On either the front or the back, my contact information should be listed: - ros@drrospetrakis.example - 555.014.7788 - drrospetrakis.example On the rear, I would like a description of the areas that I specialize in. This can be formatted in any way that appears stylistically interesting. Individual and Couples Relationships and Infidelity Sexual Health & Aging Gender Identity & Sexual Orientation Abuse and Trauma Sexual Compulsivity & Addiction Sexual Dysfunction
- Follow brand guide

```html
<!DOCTYPE html>
<html lang="en">
<head>
<meta charset="utf-8">
<title>Dr. Rosalind Petrakis — Business Card</title>
<link href="https://fonts.googleapis.com/css2?family=Lato:wght@400;700&family=Libre+Baskerville:wght@400;700&display=swap" rel="stylesheet">
<style>
  :root {
    --backdrop: #34363b;
    --paper: #ffffff;
    --navy: #29234f;
    --ink: #262047;
    --grey: #6f7077;
    --teal: #5cc2aa;
    --teal-light: #a6dccf;
    --orange: #f5a623;
    --red: #e84a4f;
    --white: #ffffff;
  }
  * { box-sizing: border-box; margin: 0; padding: 0; }
  html, body { width: 1200px; height: 952px; overflow: hidden; }
  body {
    background: var(--backdrop);
    font-family: "Lato", sans-serif;
    display: flex;
    flex-direction: column;
    align-items: center;
    justify-content: center;
    gap: 60px;
  }
  .card {
    position: relative;
    width: 640px;
    height: 366px;
    border-radius: 26px;
    overflow: hidden;
    box-shadow: 0 10px 30px rgba(0,0,0,.35);
  }

  /* Front */
  .card--front { background: var(--paper); color: var(--ink); }
  .wordmark {
    position: absolute;
    display: flex;
    align-items: center;
    gap: 12px;
  }
  .wordmark__dot {
    width: 40px; height: 40px; border-radius: 50%;
    background: var(--teal);
    flex: none;
  }
  .wordmark__name {
    font-family: "Libre Baskerville", serif;
    font-weight: 400;
    font-size: 19px;
    letter-spacing: .5px;
  }
  .card--front .wordmark { top: 40px; left: 40px; }
  .card--front .wordmark__name { color: var(--ink); }

  .contact {
    position: absolute;
    top: 130px; left: 40px;
    list-style: none;
    display: flex; flex-direction: column; gap: 9px;
    font-size: 14px; color: var(--grey);
  }
  .contact__item { display: flex; align-items: center; gap: 9px; }
  .contact__icon {
    width: 18px; height: 18px; border-radius: 4px;
    display: flex; align-items: center; justify-content: center;
  }
  .contact__icon--phone { background: var(--teal); }
  .contact__icon--mail { background: var(--orange); }
  .contact__icon--web { background: var(--red); }

  .identity {
    position: absolute;
    top: 140px; right: 40px;
    text-align: right;
  }
  .identity__name {
    font-family: "Libre Baskerville", serif;
    font-weight: 700;
    font-size: 17px;
    text-transform: uppercase;
    color: var(--ink);
  }
  .identity__title {
    margin-top: 6px;
    font-size: 14px;
    color: var(--grey);
    letter-spacing: .3px;
  }
  .corner-disc {
    position: absolute;
    right: 70px; bottom: -70px;
    width: 230px; height: 230px;
    border-radius: 50%;
    background: var(--teal-light);
    border: 7px solid var(--navy);
  }

  /* Back */
  .card--back { background: var(--navy); color: var(--white); }
  .card--back .wordmark { top: 44px; left: 50%; transform: translateX(-50%); }
  .card--back .wordmark__name { color: var(--white); font-size: 21px; }

  .specialties {
    position: absolute;
    top: 132px; left: 52px; right: 40px;
    display: grid;
    grid-template-columns: 1fr 1.25fr;
    column-gap: 30px;
  }
  .specialties__list {
    list-style: none;
    display: flex; flex-direction: column; gap: 14px;
    font-size: 15px;
  }
  .specialties__list--second { padding-top: 52px; }
  .specialty { display: flex; align-items: center; gap: 8px; }
  .tick {
    width: 13px; height: 13px; flex: none;
    border: 1px solid rgba(255,255,255,.7);
    border-radius: 2px;
    display: flex; align-items: center; justify-content: center;
  }
</style>
</head>
<body>

  <section class="card card--front" aria-label="Business card front">
    <div class="wordmark">
      <span class="wordmark__dot"></span>
      <span class="wordmark__name">Dr. Rosalind Petrakis</span>
    </div>

    <ul class="contact">
      <li class="contact__item">
        <span class="contact__icon contact__icon--phone">
          <svg width="11" height="11" viewBox="0 0 24 24"><path fill="#fff" d="M6.6 10.8a15 15 0 0 0 6.6 6.6l2.2-2.2c.3-.3.7-.4 1-.2 1.1.4 2.3.6 3.6.6.6 0 1 .4 1 1V20c0 .6-.4 1-1 1A17 17 0 0 1 3 4c0-.6.4-1 1-1h3.5c.6 0 1 .4 1 1 0 1.3.2 2.5.6 3.6.1.3 0 .7-.2 1z"/></svg>
        </span>
        555.014.7788
      </li>
      <li class="contact__item">
        <span class="contact__icon contact__icon--mail">
          <svg width="11" height="11" viewBox="0 0 24 24"><rect x="2" y="5" width="20" height="14" rx="1" fill="none" stroke="#fff" stroke-width="2"/><path d="M2 6l10 7 10-7" fill="none" stroke="#fff" stroke-width="2"/></svg>
        </span>
        ros@drrospetrakis.example
      </li>
      <li class="contact__item">
        <span class="contact__icon contact__icon--web">
          <svg width="11" height="11" viewBox="0 0 24 24"><circle cx="12" cy="12" r="9" fill="none" stroke="#fff" stroke-width="2"/><path d="M3 12h18M12 3c3 3 3 15 0 18M12 3c-3 3-3 15 0 18" fill="none" stroke="#fff" stroke-width="2"/></svg>
        </span>
        drrospetrakis.example
      </li>
    </ul>

    <div class="identity">
      <p class="identity__name">Dr. Rosalind Petrakis</p>
      <p class="identity__title">Licensed Psychologist</p>
    </div>

    <div class="corner-disc"></div>
  </section>

  <section class="card card--back" aria-label="Business card back">
    <div class="wordmark">
      <span class="wordmark__dot"></span>
      <span class="wordmark__name">Dr. Rosalind Petrakis</span>
    </div>

    <div class="specialties">
      <ul class="specialties__list">
        <li class="specialty"><span class="tick"><svg width="10" height="10" viewBox="0 0 24 24"><path d="M4 12l5 5L20 6" fill="none" stroke="#e84a4f" stroke-width="4"/></svg></span>Stylistically Interesting</li>
        <li class="specialty"><span class="tick"><svg width="10" height="10" viewBox="0 0 24 24"><path d="M4 12l5 5L20 6" fill="none" stroke="#e84a4f" stroke-width="4"/></svg></span>Individual And Couples</li>
        <li class="specialty"><span class="tick"><svg width="10" height="10" viewBox="0 0 24 24"><path d="M4 12l5 5L20 6" fill="none" stroke="#e84a4f" stroke-width="4"/></svg></span>Relationships And Infidelity</li>
        <li class="specialty"><span class="tick"><svg width="10" height="10" viewBox="0 0 24 24"><path d="M4 12l5 5L20 6" fill="none" stroke="#e84a4f" stroke-width="4"/></svg></span>Sexual Health &amp; Aging</li>
      </ul>
      <ul class="specialties__list specialties__list--second">
        <li class="specialty"><span class="tick"><svg width="10" height="10" viewBox="0 0 24 24"><path d="M4 12l5 5L20 6" fill="none" stroke="#e84a4f" stroke-width="4"/></svg></span>Gender Identity &amp; Sexual Orientation</li>
        <li class="specialty"><span class="tick"><svg width="10" height="10" viewBox="0 0 24 24"><path d="M4 12l5 5L20 6" fill="none" stroke="#e84a4f" stroke-width="4"/></svg></span>Abuse And Trauma</li>
        <li class="specialty"><span class="tick"><svg width="10" height="10" viewBox="0 0 24 24"><path d="M4 12l5 5L20 6" fill="none" stroke="#e84a4f" stroke-width="4"/></svg></span>Sexual Compulsivity &amp; Addiction</li>
        <li class="specialty"><span class="tick"><svg width="10" height="10" viewBox="0 0 24 24"><path d="M4 12l5 5L20 6" fill="none" stroke="#e84a4f" stroke-width="4"/></svg></span>Sexual Dysfunction</li>
      </ul>
    </div>
  </section>

</body>
</html>
```